Business card design

I need my logo on this card, things I need the card to have on it
licensed and insured.
owner operators Derek & Milton Halvorsen
my phone number 5418237906
Disaster Recovery, Storm Damage Restoration, Proactive Disaster Plan Management, Roof Repair/Restoration Structural Repair and Reconstruction, Emergency Boarding and Tarping Service, Perimeter Fencing, Emergency Tree Removal,

```html
<!DOCTYPE html>
<html lang="en">
<head>
<meta charset="UTF-8">
<title>Ridgeline Construction – Business Card</title>
<link href="https://fonts.googleapis.com/css2?family=Montserrat:wght@400;500&family=Saira+Extra+Condensed:wght@600&display=swap" rel="stylesheet">
<style>
  :root {
    --backdrop: #d9d3ca;
    --card: #4a4e63;
    --card-edge: #42465a;
    --brand-blue: #2f9be0;
    --accent-red: #e23a4c;
    --text-light: #d6d8e0;
    --text-muted: #aeb1c0;
  }
  * { margin: 0; padding: 0; box-sizing: border-box; }
  html, body {
    width: 1200px;
    height: 800px;
    overflow: hidden;
    background: var(--backdrop);
  }
  .stage {
    width: 1200px;
    height: 800px;
    display: flex;
    align-items: center;
    justify-content: center;
  }
  .business-card {
    width: 980px;
    height: 560px;
    background: var(--card);
    border: 1px solid var(--card-edge);
    display: flex;
    flex-direction: column;
    align-items: center;
    padding-top: 70px;
    text-align: center;
    font-family: "Montserrat", sans-serif;
  }
  .brand {
    display: flex;
    align-items: center;
    gap: 14px;
    color: var(--brand-blue);
    font-family: "Montserrat", sans-serif;
    font-weight: 400;
    font-size: 36px;
    letter-spacing: 2px;
    white-space: nowrap;
  }
  .brand-mark {
    width: 22px;
    height: 22px;
    background: var(--brand-blue);
  }
  .owners {
    margin-top: 64px;
    font-family: "Saira Extra Condensed", "Roboto Condensed", "Arial Narrow", sans-serif;
    font-stretch: condensed;
    font-weight: 600;
    font-size: 58px;
    letter-spacing: 7px;
    color: var(--accent-red);
    line-height: 1;
    white-space: nowrap;
  }
  .phone {
    margin-top: 12px;
    font-size: 21px;
    color: var(--text-light);
    letter-spacing: 0.5px;
  }
  .phone-label { color: var(--accent-red); font-weight: 500; }
  .services {
    margin-top: 54px;
    list-style: none;
    font-size: 16px;
    line-height: 1.65;
    color: var(--text-light);
    white-space: nowrap;
  }
  .sep { color: var(--accent-red); padding: 0 6px; }
  .credentials {
    margin-top: 22px;
    font-size: 13px;
    letter-spacing: 4px;
    text-transform: uppercase;
    color: var(--text-muted);
  }
</style>
</head>
<body>
  <main class="stage">
    <section class="business-card">
      <div class="brand">
        <span class="brand-mark" aria-hidden="true"></span>
        <span class="brand-name">RIDGELINE CONSTRUCTION L.L.C</span>
      </div>
      <h1 class="owners">DEREK &amp; MILTON HALVORSEN</h1>
      <p class="phone"><span class="phone-label">P:</span> 541-823-7906</p>
      <ul class="services">
        <li>Disaster Recovery<span class="sep">•</span>Perimeter Fencing<span class="sep">•</span>Emergency Tree Removal</li>
        <li>Structural Repair and Reconstruction<span class="sep">•</span>Emergency Boarding and Tarping Service</li>
        <li>Roof Repair/Restoration<span class="sep">•</span>Storm Damage Restoration<span class="sep">•</span>Proactive Disaster Plan Management</li>
      </ul>
      <p class="credentials">Licensed and Insured</p>
    </section>
  </main>
</body>
</html>
```